Brantley Yard Services Flyer Design

I need a new flyer design for my business, Brantley Yard Services. I’ll be providing my old flyer and logo as references. The new flyer should feature updated wording, contact information, logos, and photos, but still keep the original “What We Do” section and include the phrase “Don’t See? Just Ask!” somewhere near the services. The flyer needs to look great in black and white for door-to-door handouts but also be eye-catching and professional enough for social media use.

The updated content should include the headline “Transforming Outdoor Spaces with Hard Work & Precision” and highlight three main service areas: Landscaping Services (project-based landscaping to clean, prepare, and transform outdoor spaces with precision), Property Cleanup (quick hauls, debris removal, or full cleanouts—no job too big or small), and Ground Preparation (pad preparation, brush removal, and fire lines—making properties safe, functional, and project-ready).

Please also include a “Why Choose Us?” section that lists: Locally owned since 2022, Reliable & affordable – no corners cut, Professional results you can trust, LICENSED AND Insured, and Quality work / on time / references / flexible / follow-up.

At the bottom, include the contact details: Call or Text Today!
www.brantleyyard.example
| sales@brantleyyard.example
| (555) 014-2793

The overall design should be clean, professional, and easy to read with a layout that clearly shows what we offer. Use visuals that represent outdoor services, landscaping, and property cleanup/prep work. I want something that feels trustworthy, family-friendly, and modern.
Use the same photo of leaf clean up from the original flyer if possible.
Our company colors are also black and white. For the most part.

```html
<!DOCTYPE html>
<html lang="en">
<head>
<meta charset="utf-8">
<title>Brantley Yard Services Flyer</title>
<link href="https://fonts.googleapis.com/css2?family=Exo+2:ital,wght@0,400;0,600;0,800;1,800;1,900&display=swap" rel="stylesheet">
<style>
  :root {
    --ink: #111111;
    --paper: #ffffff;
    --backdrop: #e4e4e4;
  }
  * { box-sizing: border-box; margin: 0; padding: 0; }
  html, body {
    width: 1200px; height: 1200px; overflow: hidden;
    background: var(--backdrop);
    font-family: "Exo 2", sans-serif;
    color: var(--ink);
  }
  .flyer {
    position: absolute; left: 203px; top: 40px;
    width: 794px; height: 1120px;
    background: var(--paper);
    overflow: hidden;
  }
  .flyer > * { position: absolute; }
  .corner-frame { left: 0; top: 0; }
  .brand {
    left: 52px; top: 44px;
    display: flex; align-items: center; gap: 12px;
  }
  .brand-mark { width: 22px; height: 22px; background: var(--ink); }
  .brand-name {
    font-weight: 800; font-size: 27px; line-height: 1;
    text-transform: uppercase; letter-spacing: 0.5px;
  }
  .headline {
    right: 55px; top: 110px;
    text-align: right;
    font-style: italic; font-weight: 900;
    font-size: 47px; line-height: 56px;
    text-transform: uppercase; letter-spacing: 1px;
  }
  .services { left: 52px; top: 368px; width: 680px; }
  .service { margin-bottom: 20px; }
  .service h2 { font-weight: 800; font-size: 19px; line-height: 22px; letter-spacing: 0.3px; }
  .service p { font-size: 14.5px; line-height: 19px; }
  .offer-frame { left: 0; top: 0; }
  .tab {
    color: var(--paper); font-weight: 600; font-size: 27px;
    display: flex; align-items: center; justify-content: center;
  }
  .tab-offer { left: 278px; top: 608px; width: 237px; height: 45px; }
  .tab-why { left: 258px; top: 885px; width: 282px; height: 44px; }
  .tab span { position: relative; }
  .tab svg { position: absolute; left: 0; top: 0; }
  .offer-columns { left: 52px; top: 688px; width: 700px; }
  .offer-col { position: absolute; top: 0; }
  .offer-col h3 { font-weight: 800; font-size: 19px; line-height: 24px; }
  .offer-col li { list-style: none; font-size: 14.5px; line-height: 19px; }
  .col-remove { left: 0; }
  .col-install { left: 288px; }
  .col-maintain { left: 435px; }
  .ask { left: 0; width: 100%; top: 828px; text-align: center; font-weight: 800; font-size: 20px; }
  .why-text {
    left: 60px; width: 674px; top: 940px;
    text-align: center; font-size: 14.5px; line-height: 19px;
  }
  .cta { left: 0; width: 100%; top: 1030px; text-align: center; font-weight: 600; font-size: 20px; }
  .contact-bar {
    left: 0; top: 1067px; width: 794px; height: 26px;
    background: var(--ink); color: var(--paper);
    font-size: 15px; font-weight: 600;
  }
  .contact-bar span { position: absolute; top: 0; height: 26px; line-height: 26px; white-space: nowrap; }
  .contact-phone { left: 128px; }
  .contact-email {
    left: 262px; top: 4px !important; height: 22px !important; line-height: 20px !important;
    padding: 0 16px 0 10px;
    background: var(--paper); color: var(--ink);
    clip-path: polygon(0 0, 100% 0, 100% 60%, calc(100% - 9px) 100%, 0 100%);
  }
  .contact-web { left: 500px; }
</style>
</head>
<body>
<main class="flyer">
  <svg class="corner-frame" width="794" height="1120" viewBox="0 0 794 1120" aria-hidden="true">
    <polygon points="376,0 794,0 794,520 760,571 760,45 411,45 130,318" fill="var(--ink)"/>
  </svg>

  <div class="brand">
    <div class="brand-mark"></div>
    <div class="brand-name">Brantley Yard<br>Services</div>
  </div>

  <h1 class="headline">Transforming<br>Outdoor Spaces<br>With Hard Work<br>&amp; Precision</h1>

  <section class="services">
    <div class="service">
      <h2>Landscaping Services</h2>
      <p>project-based landscaping to clean, prepare, and transform outdoor spaces with<br>precision</p>
    </div>
    <div class="service">
      <h2>Property Cleanup</h2>
      <p>quick hauls, debris removal, or full cleanouts—no job too big or small</p>
    </div>
    <div class="service">
      <h2>Ground Preparation</h2>
      <p>pad preparation, brush removal, and fire lines—making properties safe, functional, and<br>project-ready</p>
    </div>
  </section>

  <svg class="offer-frame" width="794" height="1120" viewBox="0 0 794 1120" aria-hidden="true">
    <polygon points="75,607 760,607 760,767 712,815 34,815 34,654" fill="none" stroke="var(--ink)" stroke-width="1.5"/>
  </svg>

  <div class="tab tab-offer">
    <svg width="237" height="45" viewBox="0 0 237 45" aria-hidden="true">
      <polygon points="0,0 222,0 237,14 237,45 14,45 0,31" fill="var(--ink)"/>
    </svg>
    <span>What We Do</span>
  </div>

  <section class="offer-columns">
    <div class="offer-col col-remove">
      <h3>Remove</h3>
      <ul><li>Junk Removal</li><li>Trash &amp; waste hauling</li><li>Yard and garden cleanup</li><li>Appliance removal</li></ul>
    </div>
    <div class="offer-col col-install">
      <h3>Install</h3>
      <ul><li>Mulch</li><li>D.G.</li><li>Plants</li><li>Rock</li></ul>
    </div>
    <div class="offer-col col-maintain">
      <h3>Maintenance &amp; Other</h3>
      <ul><li>Yard clean up</li><li>Weed prevention (pre-emergent)</li><li>Roof &amp; gutter cleaning</li><li>Fence &amp; deck staining</li></ul>
    </div>
  </section>

  <p class="ask">Don’t See? Just Ask!</p>

  <div class="tab tab-why">
    <svg width="282" height="44" viewBox="0 0 282 44" aria-hidden="true">
      <polygon points="0,0 267,0 282,14 282,44 14,44 0,30" fill="var(--ink)"/>
    </svg>
    <span>Why Choose Us?</span>
  </div>

  <p class="why-text">Locally owned since 2022, Reliable &amp; affordable – no corners cut, Professional<br>results you can trust, LICENSED AND Insured, and Quality work / on time /<br>references / flexible / follow-up.</p>

  <p class="cta">Call or Text Today!</p>

  <footer class="contact-bar">
    <span class="contact-phone">(555) 014-2793</span>
    <span class="contact-email">sales@brantleyyard.example</span>
    <span class="contact-web">www.brantleyyard.example</span>
  </footer>
</main>
</body>
</html>
```